Personal Trainer Business Card

I need a business card using a logo I already have.
The logo is in uploaded files.
Card is to give to prospective clients that interested in health and beauty or already exercise. Would like logo on front or other abstract images and details on back.
Like modern design that also unique and eye catching rather than just generic fitness gym/fitness theme.

Target Market(s)

Main clients are trendy women aged 25-60.

Industry/Entity Type

Fitness

Contact Information for Business Card

Email: tom@tomharvecoaching.com

web: www.tomharvecoaching.com

mobile: 0493 257618

facebook: www.facebook.com/tomharvecoaching

Location is: Sunshine Coast

Font styles to use
Sans Serif

Colors
000000
1b1b1b
333333

Requirements
Must have
• Logo on front
• black background of sorts on front (fine if mixed with dark grey or abstract)
• White background on back.
Nice to have
• I would like the front side with the logo appearing on it with black background. Fine with alternative ideas and layout.
• Would like the front to be modern, professional and cool/interesting.
• Fine with abstract or modern design.
• Reverse of the card some white background with details on it
• (I like simple fonts).
• CAn use same font colour as in logo in places or what whatever
Should not have
• Avoiding use of cheap pics such as weights

```html
<!DOCTYPE html>
<html lang="en">
<head>
<meta charset="utf-8">
<title>Tom Harve Coaching – Business Card</title>
<link rel="stylesheet" href="https://fonts.googleapis.com/css2?family=Montserrat:wght@500;700;800&display=swap">
<style>
  :root {
    --page: #eeeeee;
    --black: #000000;
    --charcoal: #1b1b1b;
    --graphite: #333333;
    --gold: #c9a227;
    --gold-light: #fbf494;
    --gold-mid: #e2c84a;
    --paper: #fdfdf9;
    --font: "Montserrat", Arial, sans-serif;
  }
  * { margin: 0; padding: 0; box-sizing: border-box; }
  html, body { width: 1200px; height: 1200px; overflow: hidden; }
  body { background: var(--page); font-family: var(--font); position: relative; }

  .brand-mark {
    position: absolute; left: 70px; top: 90px;
    color: var(--gold); font-weight: 800; text-transform: uppercase;
    font-size: 46px; line-height: 1.05; letter-spacing: 1px;
  }

  .card {
    position: absolute; width: 560px; height: 320px; overflow: hidden;
    box-shadow: 0 2px 0 #d8d8d8, 0 4px 0 #e4e4e4, 0 6px 0 #d6d6d6, 0 14px 26px rgba(0,0,0,.18);
  }

  /* Front: black side */
  .card-front { left: 580px; top: 300px; background: linear-gradient(160deg, var(--charcoal), var(--black) 70%); }
  .card-front .wedge { position: absolute; inset: 0; }
  .card-front .name {
    position: absolute; left: 150px; top: 60px;
    color: var(--gold); font-weight: 800; font-size: 34px; line-height: 1.05; text-transform: uppercase;
  }
  .card-front .location {
    position: absolute; left: 40px; top: 170px;
    color: var(--gold); font-weight: 500; font-size: 10px; letter-spacing: 1px; text-transform: uppercase;
  }
  .card-front .location-rule {
    position: absolute; left: 40px; top: 188px; width: 150px; height: 2px; background: var(--gold);
  }
  .contact {
    position: absolute; right: 34px; bottom: 34px; list-style: none;
    color: var(--black); font-weight: 700; font-size: 12px; text-align: right;
  }
  .contact li { display: flex; align-items: center; justify-content: flex-end; gap: 8px; height: 24px; }
  .contact li.phone { font-size: 16px; font-weight: 800; letter-spacing: 1px; }
  .contact svg { width: 18px; height: 18px; flex: none; }

  /* Back: white side */
  .card-back { left: 60px; top: 720px; background: var(--paper); }
  .card-back .name {
    position: absolute; left: 60px; top: 90px;
    color: var(--gold); font-weight: 800; font-size: 46px; line-height: 1.05; text-transform: uppercase;
  }
  .card-back .web {
    position: absolute; left: 60px; bottom: 40px;
    color: var(--black); font-weight: 700; font-size: 12px; letter-spacing: 1px; text-transform: uppercase;
  }
</style>
</head>
<body>

  <div class="brand-mark">Tom Harve<br>Coaching</div>

  <section class="card card-front">
    <svg class="wedge" viewBox="0 0 560 320" preserveAspectRatio="none" aria-hidden="true">
      <defs>
        <linearGradient id="goldBand" x1="0" y1="1" x2="1" y2="0">
          <stop offset="0" stop-color="var(--gold)"/>
          <stop offset="0.55" stop-color="var(--gold-light)"/>
          <stop offset="1" stop-color="var(--gold-mid)"/>
        </linearGradient>
      </defs>
      <polygon points="0,290 560,100 560,320 0,320" fill="url(#goldBand)"/>
      <polygon points="40,320 560,140 560,150 60,320" fill="var(--black)" opacity="0"/>
      <rect x="0" y="308" width="560" height="12" fill="var(--black)"/>
      <rect x="548" y="100" width="12" height="220" fill="var(--black)"/>
    </svg>
    <div class="name">Tom Harve<br>Coaching</div>
    <p class="location">Sunshine Coast</p>
    <div class="location-rule"></div>
    <ul class="contact">
      <li class="phone">0493 257618
        <svg viewBox="0 0 24 24"><rect x="6" y="2" width="12" height="20" rx="2.5" fill="none" stroke="currentColor" stroke-width="2"/><circle cx="12" cy="18" r="1.2" fill="currentColor"/></svg>
      </li>
      <li>tom@tomharvecoaching.com
        <svg viewBox="0 0 24 24"><rect x="2" y="5" width="20" height="14" rx="1.5" fill="currentColor"/><path d="M3 6l9 7 9-7" fill="none" stroke="var(--gold-light)" stroke-width="1.6"/></svg>
      </li>
      <li>/tomharvecoaching
        <svg viewBox="0 0 24 24"><rect x="3" y="3" width="18" height="18" rx="3" fill="currentColor"/></svg>
      </li>
      <li>www.tomharvecoaching.com
        <svg viewBox="0 0 24 24" fill="none" stroke="currentColor" stroke-width="1.8"><circle cx="12" cy="12" r="9"/><ellipse cx="12" cy="12" rx="4" ry="9"/><path d="M3 12h18M5 7h14M5 17h14"/></svg>
      </li>
    </ul>
  </section>

  <section class="card card-back">
    <div class="name">Tom Harve<br>Coaching</div>
    <p class="web">www.tomharvecoaching.com</p>
  </section>

</body>
</html>
```